Movie Poster/DVD jacket for Short Documentary

I am a documentary filmmaker who just completed a project titled "Sister Marigold". Here is the logline (short description of the movie): "An Oklahoma family is ripped apart after their 15-year-old son brutally murders his older sister in 1974. Controversy swirls around the case after his parents decide to hire a prominent defense attorney to keep him out of jail." I have several good photos of the family involved. I am in the process of submitting the film to several festivals and I want a professional looking movie poster that can be sent with film submissions. The look needs to dramatic and serious.
Updates

Project Deadline Extended Reason: We just had several more submission enter today and need a few more days to evaluate. Thank you for you patience. Added Thursday, November 19, 2015

Target Market(s)

Film festivals, television

Industry/Entity Type

Movie

Colors
f04a50

Requirements
Must have
• the color red and have a similar appearance to the sample movie posters.
• Also, tagline: turning a blind eye into broken hearts
• Directors name: a film by Rob Haskett
Nice to have
• rough
Should not have
• Not a gruesome look.

```html
<!DOCTYPE html>
<html lang="en">
<head>
<meta charset="utf-8">
<title>Sister Marigold — a film by Rob Haskett</title>
<link rel="stylesheet" href="https://fonts.googleapis.com/css2?family=Montserrat:wght@700;800&family=Old+Standard+TT:wght@400;700&display=swap">
<style>
  :root {
    --poster-red: #8a171b;
    --poster-red-deep: #6c1013;
    --ink: rgba(40, 5, 7, 0.8);
    --ink-strong: rgba(22, 3, 4, 0.85);
    --frame-dark: #2a0709;
    --photo-border: #cdbf98;
    --photo-light: #d8d0b6;
    --photo-mid: #a39d8c;
    --photo-dark: #4b4841;
    --title-white: #f4f2ee;
  }
  * { margin: 0; padding: 0; box-sizing: border-box; }
  html, body { width: 863px; height: 1200px; overflow: hidden; background: var(--poster-red); }
  .poster {
    position: relative; width: 863px; height: 1200px; overflow: hidden;
    background: radial-gradient(ellipse at 40% 45%, #92191d 0%, var(--poster-red) 55%, var(--poster-red-deep) 100%);
    font-family: "Old Standard TT", "Times New Roman", serif;
    color: var(--ink);
  }

  /* clipping type */
  .headline {
    position: absolute; left: 80px; top: -22px;
    font-weight: 700; font-size: 54px; line-height: 88px; color: var(--ink);
  }
  .col-grid { position: absolute; display: flex; gap: 16px; overflow: hidden; }
  .column {
    flex: 1; font-size: 16px; line-height: 21px; text-align: justify; color: var(--ink);
  }
  .flipped { transform: rotate(180deg); }
  .big-flipped {
    position: absolute; font-weight: 700; font-size: 54px; line-height: 1;
    color: var(--ink); transform: rotate(180deg); white-space: nowrap;
  }
  .big-court { left: 496px; top: 158px; }
  .big-term { left: 703px; top: 228px; }
  .dateline {
    position: absolute; left: 808px; top: 300px; font-size: 16px; color: var(--ink);
    transform: rotate(90deg); transform-origin: left top; white-space: nowrap;
  }

  /* photo block */
  .frame-shadow { position: absolute; left: 33px; top: 144px; width: 749px; height: 673px; background: var(--frame-dark); opacity: 0.8; }
  .photo {
    position: absolute; left: 111px; top: 186px; width: 693px; height: 657px;
    background: linear-gradient(160deg, var(--photo-light) 0%, var(--photo-mid) 45%, var(--photo-dark) 100%);
    border: 14px solid var(--photo-border); opacity: 0.9;
  }
  .photo-shade { position: absolute; left: 111px; top: 186px; width: 62px; height: 657px; background: rgba(20, 4, 5, 0.5); }

  .story {
    position: absolute; left: 80px; top: 246px; width: 372px;
    font-size: 18px; line-height: 29px; color: var(--ink-strong);
  }
  .story .byline { font-size: 15px; }
  .story .see { font-weight: 700; margin-left: 30px; }
  .rule { position: absolute; left: 295px; top: 922px; width: 110px; height: 2px; background: var(--ink); }

  .top-right { left: 438px; top: -45px; width: 425px; height: 180px; }
  .inset-cols { left: 502px; top: 531px; width: 156px; height: 277px; opacity: 0.7; }
  .bottom-cols { left: 0; top: 912px; width: 606px; height: 330px; }
  .side-cols {
    left: 863px; top: 555px; width: 680px; height: 257px;
    transform: rotate(90deg); transform-origin: left top; opacity: 0.9;
  }

  /* title lockup */
  .title-layer { position: absolute; left: 0; top: 0; width: 863px; height: 1200px; }
  .tagline { font-family: "Montserrat", Arial, sans-serif; font-weight: 700; fill: var(--title-white); }
  .title { font-family: "Montserrat", Arial, sans-serif; font-weight: 800; fill: var(--title-white); }
  .credit { font-family: "Montserrat", Arial, sans-serif; font-weight: 700; fill: var(--title-white); }
</style>
</head>
<body>
<main class="poster">
  <h2 class="headline">Boy jailed<br>after farm<br>shooting</h2>

  <div class="col-grid top-right flipped">
    <p class="column">County officials met Friday morning to review the case file, which was forwarded from the sheriff's office late Thursday. A hearing date has not been set, and the family's attorney declined to comment on the matter when reached by telephone at his office downtown this week.</p>
    <p class="column">The judge is expected to rule within the month on whether the youth will face charges in adult court. Neighbors described the family as quiet and well liked in the small community east of town, where the boy attended the consolidated high school until this fall.</p>
  </div>
  <div class="big-flipped big-court">Court Date</div>
  <div class="big-flipped big-term">Juvenile</div>
  <div class="dateline">Nov. 8, 1974, Section B, Page 6</div>

  <div class="frame-shadow"></div>
  <div class="photo" role="img" aria-label="Faded 1970s family snapshot of a child at home"></div>
  <div class="photo-shade"></div>

  <div class="story">
    <p class="byline">By Wade Ellison</p>
    <p>REDBANK—Neighbors along the gravel road east of town said Thursday they heard nothing unusual before deputies arrived at the farmhouse shortly after dark. The family had lived on the property for nearly twenty years and were known at the local church. Sheriff Harlan Pruitt said investigators stayed at the home through the night and that no further arrests were expected. Services for the young woman are pending at a chapel in Cold Springs, where she had lived with her husband since they married last spring.</p>
    <p>The youth remains in the county jail pending a hear-</p>
    <p class="see">(See HEARING—Page 3)</p>
  </div>
  <div class="rule"></div>

  <div class="col-grid inset-cols flipped">
    <p class="column">the defense has asked that the hearing be closed to the public, citing the age of the accused and the wishes of the family. Judge Vernon Lee Tate is expected to decide the request next week.</p>
  </div>

  <div class="col-grid bottom-cols flipped">
    <p class="column">Attorneys for the family said Monday they would ask the court to keep the case in juvenile court. Earl Hadley, the assistant prosecutor, said his office had not yet decided whether to appeal. The boy was described by teachers as a good student who kept to himself.</p>
    <p class="column">Marigold is being held under bond set last week by Judge Vernon Lee Tate. No date has been set for a further hearing. Relatives from out of state arrived Sunday to be with the parents, who have not spoken publicly about the events at the farm.</p>
    <p class="column">Harmon Ridge County records show the family bought the land in 1955. A brother-in-law, Dale Emmett Crane, was away on business at the time, officers said. Deputies returned to the home Saturday to collect further statements from family members.</p>
    <p class="column">The case has drawn wide attention across the county, with letters to the editor arriving daily. Church leaders asked residents to keep the family in their prayers and to refrain from gossip while the matter remains before the court.</p>
  </div>

  <div class="col-grid side-cols">
    <p class="column">the county attorney's office filed a motion Tuesday asking that the youth be tried as an adult, a request the defense said it would oppose at every step. The motion will be heard before the district court later this month, officials said.</p>
    <p class="column">the family home sits at the end of a long lane off the state highway. Mrs. Crane had driven up with her husband to spend the holiday weekend with her parents and younger brother, according to a statement issued by deputies on Friday.</p>
    <p class="column">He said no ruling has been made on the motion. Meanwhile, the boy remains in custody and has been visited daily by his parents and their pastor, who asked that the community show patience and kindness during this time.</p>
  </div>

  <svg class="title-layer" viewBox="0 0 863 1200" role="img" aria-label="Sister Marigold, a film by Rob Haskett">
    <text class="tagline" x="433" y="334" text-anchor="middle" font-size="22" textLength="539" lengthAdjust="spacingAndGlyphs">turning a blind eye into broken hearts</text>
    <text class="title" x="51" y="470" font-size="124" textLength="755" lengthAdjust="spacingAndGlyphs">SISTER</text>
    <text class="title" x="0" y="560" font-size="124" textLength="863" lengthAdjust="spacingAndGlyphs">MARIGOLD</text>
    <text class="credit" x="398" y="605" text-anchor="middle" font-size="21">a film by</text>
    <text class="credit" x="437" y="650" text-anchor="middle" font-size="30" letter-spacing="1">R<tspan font-size="23">OB</tspan> H<tspan font-size="23">ASKETT</tspan></text>
  </svg>
</main>
</body>
</html>
```